Business Card Design Project

Create an impressive business care to use
Updates

My logo is available at http://corvalune.example, or

Industry/Entity Type

Business

Requirements
Must have
• company logo

```html
<!DOCTYPE html>
<html lang="en">
<head>
<meta charset="UTF-8">
<title>Corvalune Research Corporation – Business Card</title>
<link rel="stylesheet" href="https://fonts.googleapis.com/css2?family=Lato:wght@400;700;900&family=Noto+Sans+SC:wght@400&display=swap">
<style>
  :root {
    --backdrop: #3b3b3b;
    --card: #ffffff;
    --ink: #1f1f1f;
    --green: #1f9a4c;
    --blue: #1aa3df;
    --orange: #f6a93b;
    --lime: #8cc13f;
  }
  * { margin: 0; padding: 0; box-sizing: border-box; }
  html, body { width: 1200px; height: 900px; overflow: hidden; }
  body {
    background: var(--backdrop);
    font-family: "Lato", sans-serif;
    color: var(--ink);
    position: relative;
  }
  .card {
    position: absolute;
    top: 308px;
    width: 514px;
    height: 284px;
    background: var(--card);
    overflow: hidden;
    box-shadow: 0 3px 8px rgba(0,0,0,0.45);
  }
  .card--front { left: 72px; }
  .card--back { left: 615px; }

  .front-glow {
    position: absolute;
    left: 72px; top: -10px;
    width: 380px; height: 300px;
    border-radius: 50%;
    background:
      radial-gradient(ellipse at 35% 40%, rgba(140,193,63,0.14), transparent 60%),
      radial-gradient(ellipse at 60% 55%, rgba(26,163,223,0.14), transparent 62%),
      radial-gradient(ellipse at 55% 35%, rgba(246,169,59,0.12), transparent 58%);
  }
  .wordmark {
    display: flex;
    align-items: center;
    gap: 10px;
    font-weight: 900;
    color: var(--ink);
    letter-spacing: 0.16em;
    line-height: 1;
  }
  .wordmark__dot {
    border-radius: 50%;
    background: var(--orange);
    flex: none;
  }
  .tagline {
    color: var(--green);
    font-weight: 400;
    letter-spacing: 0.32em;
    line-height: 1;
  }
  .card--front .brand {
    position: absolute;
    left: 86px; top: 112px;
  }
  .card--front .wordmark { font-size: 42px; }
  .card--front .wordmark__dot { width: 26px; height: 26px; }
  .card--front .tagline { font-size: 15px; margin-top: 10px; margin-left: 2px; }

  .back-glow {
    position: absolute;
    right: -10px; top: -20px;
    width: 245px; height: 200px;
    border-radius: 50%;
    background:
      radial-gradient(ellipse at 30% 40%, var(--lime) 0%, transparent 55%),
      radial-gradient(ellipse at 45% 60%, var(--blue) 0%, transparent 60%),
      radial-gradient(ellipse at 70% 50%, var(--orange) 0%, transparent 62%);
    opacity: 0.85;
  }
  .card--back .brand {
    position: absolute;
    left: 28px; top: 30px;
  }
  .card--back .wordmark { font-size: 27px; gap: 7px; }
  .card--back .wordmark__dot { width: 16px; height: 16px; }
  .card--back .tagline { font-size: 10px; margin-top: 6px; letter-spacing: 0.36em; }

  .person {
    position: absolute;
    left: 43px; top: 108px;
  }
  .person__name { color: var(--blue); font-weight: 700; font-size: 14px; }
  .person__native { font-family: "Noto Sans SC", sans-serif; font-size: 13px; margin-top: 2px; }
  .person__role { font-size: 14px; margin-top: 2px; }

  .office {
    position: absolute;
    top: 182px;
    font-size: 10.5px;
    line-height: 13.5px;
  }
  .office--us { left: 43px; }
  .office--cn { left: 293px; }
  .office__label { font-weight: 700; }
  .office__native { font-family: "Noto Sans SC", sans-serif; font-size: 10px; color: #555; letter-spacing: 0.05em; }
  .office__web { color: var(--blue); }
  .office b { font-weight: 700; }
</style>
</head>
<body>
  <section class="card card--front" aria-label="Card front">
    <div class="front-glow" role="img" aria-label="Soft tinted circular brand decoration"></div>
    <div class="brand">
      <div class="wordmark"><span class="wordmark__dot"></span>CORVALUNE</div>
      <div class="tagline">RESEARCH CORPORATION</div>
    </div>
  </section>

  <section class="card card--back" aria-label="Card back">
    <div class="back-glow" role="img" aria-label="Coloured circular brand decoration"></div>
    <div class="brand">
      <div class="wordmark"><span class="wordmark__dot"></span>CORVALUNE</div>
      <div class="tagline">RESEARCH CORPORATION</div>
    </div>

    <div class="person">
      <p class="person__name">Marcus Lin Tao, PhD</p>
      <p class="person__native">林涛 博士</p>
      <p class="person__role">CEO</p>
    </div>

    <div class="office office--us">
      <p class="office__label">U.S.</p>
      <p>2480 Harborview Way, Suite 210</p>
      <p>Westhaven, CA 92188</p>
      <p><b>E:</b> mlin@corvalune.example</p>
      <p><b>P:</b> 555-014-2276</p>
      <p class="office__web">www.corvalune.example</p>
    </div>

    <div class="office office--cn">
      <p class="office__label">China</p>
      <p>1806, NO.48 Linhe Road</p>
      <p>Linhe District, Beijing</p>
      <p>China 100456</p>
      <p class="office__native">北京市临河区临河路48号星湾大厦</p>
      <p class="office__web">www.lumetra.example</p>
    </div>
  </section>
</body>
</html>
```